Double sided flyer for industrial investment firm

We need a A4 double sided flyer (1 page, see attached draft), which we will fold in the midle. Text is attached. What is missing is a professional and clean looking design. Text length can not be changed. it is all in German, but that should not influence the design. The flyer is added to a letter which we send to small industrial companies as an introduction to us as an investor.

What is important?
- No fancy, colorful and funny designs.
- We want a clean, professional almost minimalist design. it does not take much design elements.
- Format either landscape or vertical, whatever works best.
- stay with the colors of our company (grey, blue). see www.velkor-ag.ch for details.
- Currently used graphic in the document should be used, but is not a must. Otherwise stay with pictures or Swiss Alps (if more pictures are needed). will upload some pictures as examples.

Format for the finished flyer: InDesign and Word document or similar.
Updates

The flyer will be folded in the middle so that it becomes A5. all current designs work only as a A4 format. An A4 folded has basically 4 pages, each being A5 size. Please adapt the design accordingly.

Target Market(s)

Owners of small to medium industrial companies in Switzerland

Industry/Entity Type

Industrial

Font styles to use
Serif
Sans Serif

Colors
0255a3
3276b5
85abd2
cedeed

Requirements
Must have
• 1 page, double sided. folded in the middle. A4 Format

```html
<!DOCTYPE html>
<html lang="de">
<head>
<meta charset="utf-8">
<title>Velkor AG – Wer sind wir?</title>
<link href="https://fonts.googleapis.com/css2?family=Lato:wght@300;400;700&display=swap" rel="stylesheet">
<style>
  :root {
    --blue-deep: #0255a3;
    --blue-mid: #3276b5;
    --blue-soft: #85abd2;
    --blue-pale: #cedeed;
    --ink: #2f2f2f;
    --ink-heading: #4a4a4a;
    --ink-light: #6f6f6f;
    --paper: #ffffff;
  }
  * { box-sizing: border-box; margin: 0; padding: 0; }
  html, body { width: 1200px; height: 851px; overflow: hidden; background: var(--paper); }
  body { font-family: "Lato", Arial, sans-serif; position: relative; color: var(--ink); }

  .frame { position: absolute; inset: 0; width: 1200px; height: 851px; }

  .wave-band {
    position: absolute; left: 440px; top: 0; width: 660px; height: 115px;
    background: linear-gradient(170deg, rgba(206,222,237,0) 20%, rgba(206,222,237,.9) 45%, rgba(133,171,210,.35) 60%, rgba(206,222,237,0) 80%);
  }

  .col { position: absolute; }
  .ln { display: block; white-space: nowrap; text-align: justify; text-align-last: justify; }
  .ln.end { text-align-last: left; }

  /* left panel */
  .intro { left: 30px; top: 112px; width: 244px; color: var(--paper); }
  .intro-photo {
    width: 128px; height: 150px; border: 4px solid var(--paper);
    background: linear-gradient(180deg, #2d6fb8 0%, #6ea0d4 45%, #e9eef3 62%, #5b5f66 80%, #c9ced6 100%);
  }
  .intro-title {
    position: absolute; left: 146px; top: 18px;
    font-weight: 300; font-size: 36px; line-height: 46.5px; letter-spacing: 1px;
  }
  .intro-lead { font-size: 12.6px; line-height: 17.2px; margin-top: 16px; }
  .intro h2 { font-size: 24px; font-weight: 700; line-height: 34px; margin-top: 21px; }
  .intro-goal { font-size: 13.5px; line-height: 17.2px; margin-top: 20px; }
  .intro-goal + .intro-goal { margin-top: 25px; }

  /* main columns */
  .col h3 { font-size: 24px; font-weight: 700; color: var(--ink-heading); }

  .capital { left: 323px; top: 122px; width: 276px; }
  .capital h3 { line-height: 30px; }
  .capital p { font-size: 12.4px; line-height: 17.2px; }
  .capital .p-first { margin-top: 10px; }
  .capital h3.spaced { margin-top: 24px; }
  .capital .p-work { margin-top: 14px; }
  .capital .p-tasks { margin-top: 16px; }

  .difference { left: 643px; top: 127px; width: 245px; }
  .difference h3 { line-height: 35px; }
  .difference h3.spaced { line-height: 26px; margin-top: 17px; }
  .difference .p-fund { margin-top: 11px; }
  .difference .p-term { margin-top: 18px; }

  .history { left: 905px; top: 131px; width: 245px; }
  .history h3 { line-height: 27px; }
  .history p { margin-top: 17px; }

  .difference p, .history p {
    font-size: 11.3px; line-height: 17.2px; font-weight: 300; color: var(--ink-light);
  }

  .portrait {
    position: absolute; border: 2px solid var(--blue-deep); border-radius: 10px;
    background: linear-gradient(180deg, #f2f2f2 0%, #cfcfcf 55%, #a9a9a9 100%);
  }
  .portrait-a { left: 985px; top: 538px; width: 92px; height: 126px; }
  .portrait-b { left: 917px; top: 680px; width: 98px; height: 128px; }
  .portrait-c { left: 1040px; top: 680px; width: 96px; height: 128px; }
</style>
</head>
<body>
  <svg class="frame" viewBox="0 0 1200 851" aria-hidden="true">
    <rect x="0" y="0" width="1200" height="851" fill="#ffffff"/>
    <path d="M0 0 H300 V35 H290 V770 Q290 820 245 822 H0 Z" fill="#cfcfcf" transform="translate(6 6)"/>
    <path d="M0 0 H300 V35 H296 Q290 35 290 45 V770 Q290 820 240 820 H0 Z" fill="var(--blue-deep)"/>
    <path d="M1090 0 H1200 V851 H1165 V235 Q1165 200 1190 192 Q1165 190 1165 160 V30 H1090 Z" fill="var(--blue-deep)"/>
  </svg>

  <div class="wave-band" role="img" aria-label="Feine, geschwungene Linien als dezente Kopfdekoration"></div>

  <section class="col intro">
    <div class="intro-photo" role="img" aria-label="Verschneiter Alpengipfel unter blauem Himmel"></div>
    <h1 class="intro-title">WER<br>SIND<br>WIR?</h1>
    <p class="intro-lead">
      <span class="ln">Wir sind eine Gruppe von ca. 15</span>
      <span class="ln">Unternehmern, welche unser Kapital</span>
      <span class="ln">in mittelständische Industrieunterneh-</span>
      <span class="ln">men investieren mit einem langfristigen</span>
      <span class="ln">Ansatz. Wir haben unser Kapital in der</span>
      <span class="ln">Velkor AG gebündelt und investieren nur</span>
      <span class="ln">in eine kleine Anzahl von Unternehmen.</span>
      <span class="ln">Alle unsere Investoren sind Schweizer mit</span>
      <span class="ln">Wohnsitz in der Schweiz. Wir sind kein</span>
      <span class="ln">Private Equity Fund mit einer definierten</span>
      <span class="ln end">Haltedauer und einem Portfolio Ansatz.</span>
    </p>
    <h2>Was ist unser Ziel/<br>Vision?</h2>
    <p class="intro-goal">
      <span class="ln">Das Ziel ist nicht Grösse sondern</span>
      <span class="ln">Qualität. Wir wollen eine kleine In-</span>
      <span class="ln">dustriegruppe aufbauen mit qualitativ</span>
      <span class="ln">hochwertigen Schweizer Industrie-</span>
      <span class="ln">unternehmen, welche unabhängig</span>
      <span class="ln end">voneinander operieren.</span>
    </p>
    <p class="intro-goal">
      <span class="ln">Diesen Kredit zahlen wir in der Regel</span>
      <span class="ln">innert 3-4 Jahren zurück, da wir von</span>
      <span class="ln end">Banken unabhängig sein wollen.</span>
    </p>
  </section>

  <section class="col capital">
    <h3>Welches Kapital in-<br>vestieren wir?</h3>
    <p class="p-first">
      <span class="ln">Wir investieren unser eigenes Kapital,</span>
      <span class="ln">welches wir über die Jahre aufgebaut ha-</span>
      <span class="ln">ben. Anstatt dieses Kapital an der Börse</span>
      <span class="ln">oder in Immobilien anzulegen, kaufen wir</span>
      <span class="ln">gemeinsam ein Unternehmen und entwick-</span>
      <span class="ln">eln dieses. Wir haben mehr Vertrauen in</span>
      <span class="ln">unsere Fähigkeit eine Firma zu entwickeln</span>
      <span class="ln">als in die Finanzmärkte. Einen Teil des Kauf-</span>
      <span class="ln">preises eines Unternehmens finanzieren wir</span>
      <span class="ln end">jeweils mit einer Grossbank.</span>
    </p>
    <h3 class="spaced">Wie arbeiten wir?</h3>
    <p class="p-work">
      <span class="ln">Wir sind keine Finanzinvestoren sondern</span>
      <span class="ln">Unternehmer. Der Unterschied liegt in dem</span>
      <span class="ln">intensiven Fokus den wir auf die wenigen</span>
      <span class="ln">Firmen legen, die wir besitzen. Wir wol-</span>
      <span class="ln">len unsere Kunden und Märkte im Detail</span>
      <span class="ln">verstehen und so für das Management ein</span>
      <span class="ln">guter Diskussionspartner sein. Das bedingt,</span>
      <span class="ln">dass wir nur sehr wenige Firmen kaufen und</span>
      <span class="ln">diese dann über die Jahre ausbauen im Ge-</span>
      <span class="ln">gensatz zu einem Finanzinvestor, welcher</span>
      <span class="ln">sich an vielen Unternehmen beteiligt, um</span>
      <span class="ln">sein Risiko zu reduzieren und dann das Un-</span>
      <span class="ln end">ternehmen wieder verkauft.</span>
    </p>
    <p class="p-tasks">
      <span class="ln">Wir übernehmen operative Aufgaben und</span>
      <span class="ln">leiten gewisse Projekte, damit sich das Man-</span>
      <span class="ln">agement noch besser auf das Tagesgeschäft</span>
      <span class="ln">konzentrieren kann. Diese Arbeiten werden</span>
      <span class="ln">aber immer in Abstimmung mit dem Man-</span>
      <span class="ln">agement ausgeführt, damit jederzeit die</span>
      <span class="ln end">Führungsstruktur klar ist.</span>
    </p>
  </section>

  <section class="col difference">
    <h3>Was unterscheidet<br>uns von einem Pri-<br>vate Equity Fund?</h3>
    <p class="p-fund">
      <span class="ln">Ein Private Equity Fund kann eine geeignete</span>
      <span class="ln">Finanzierungsquelle für grössere Unterneh-</span>
      <span class="ln">men sein. Unternehmer-geführte Mittelstän-</span>
      <span class="ln">dler benötigen die Kombination von Kapital</span>
      <span class="ln">und Führung in Personalunion, um die über</span>
      <span class="ln">die Jahre etablierte Firmenkultur zu be-</span>
      <span class="ln">wahren. Ein anonymer Private Equity Fund</span>
      <span class="ln">ist da oft die falsche Lösung. Die Velkor AG</span>
      <span class="ln">als Käufer einer Firma in einer Nachfolgesitu-</span>
      <span class="ln">ation stellt die unternehmerische Kontinuität</span>
      <span class="ln">und Unabhängigkeit auch in Zukunft sicher.</span>
      <span class="ln">Wir sind transparent und langfristig orien-</span>
      <span class="ln">tiert. Ein Fond verkauft eine Beteiligung nor-</span>
      <span class="ln">malerweise nach ca. 5 Jahren, wenn der Fond</span>
      <span class="ln end">„abläuft“. So eine Frist gibt es bei Velkor nicht.</span>
    </p>
    <h3 class="spaced">Wie langfristig denk-<br>en wir?</h3>
    <p class="p-term">
      <span class="ln">Nichts ist für die Ewigkeit. Wir haben jedoch</span>
      <span class="ln">keinen festen Zeithorizont. Die Entwicklung</span>
      <span class="ln">eines Unternehmens ist eine längerfristige</span>
      <span class="ln">Aufgabe die wir mit Elan angehen. Viele Po-</span>
      <span class="ln">tentiale erkennen wir erst nach der Über-</span>
      <span class="ln">nahme und möchten diese auch umsetzen.</span>
      <span class="ln">Wir haben keinen Druck von Investoren</span>
      <span class="ln">unsere Beteiligungen zu einem bestimmten</span>
      <span class="ln">Zeitpunkt zu verkaufen. Wir bleiben solange</span>
      <span class="ln">dabei, wie wir einen Mehrwert leisten können</span>
      <span class="ln end">und das Unternehmen weiter bringen.</span>
    </p>
  </section>

  <section class="col history">
    <h3>Was haben wir bisher<br>gemacht?</h3>
    <p>
      <span class="ln">Die Velkor AG wird geführt von Urs Brändli</span>
      <span class="ln">(CEO Kochwerk AG) als Verwaltungs-</span>
      <span class="ln">ratspräsident. Die operative Leitung liegt bei</span>
      <span class="ln">Reto Kalberer (Dipl. Masch. Ing. TH)</span>
      <span class="ln">und Martin Wyss (HWV). Wir arbeiten</span>
      <span class="ln">seit ca. 10 Jahren zusammen und haben ver-</span>
      <span class="ln">schiedene Industriefirmen geführt. Unter</span>
      <span class="ln">anderem die Firma Bärtschi Maschinenbau</span>
      <span class="ln">AG in Burgdorf mit 400 Mitarbeitern, welche</span>
      <span class="ln">wir gemeinsam mit Herrn Hans Gerber</span>
      <span class="ln">(Besitzer Alpbahn und BVP Nationalrat)</span>
      <span class="ln">erworben haben. Martin Wyss und Re-</span>
      <span class="ln">to Kalberer investieren einen grossen</span>
      <span class="ln">Teil ihres Vermögens in die Velkor AG und</span>
      <span class="ln">arbeiten zu 100% für die Velkor. Die gesam-</span>
      <span class="ln">te Führung von Velkor (Verwaltungsrat und</span>
      <span class="ln">Management) verfügt über substantielle und</span>
      <span class="ln">jahrelange Erfahrung in der Führung und En-</span>
      <span class="ln end">twicklung von KMUs.</span>
    </p>
  </section>

  <div class="portrait portrait-a" role="img" aria-label="Porträtfoto des Verwaltungsratspräsidenten"></div>
  <div class="portrait portrait-b" role="img" aria-label="Porträtfoto eines Mitglieds der operativen Leitung"></div>
  <div class="portrait portrait-c" role="img" aria-label="Porträtfoto eines Mitglieds der operativen Leitung"></div>
</body>
</html>
```